Kettle Ledger Business Card design

We need a stand out business card design for Accounting practice based in Australia specialising in pubs, clubs and hotels. We help venues maximise margins, create time and manage cashflow. One club we have been working with for the last 6 months has increased revenue by 3% and margin by 5% in this time frame. We have a back office outsourced system that costs less than having a full time employee and also allows the venues the added benefit of:<br/>-using the office space to become a revenue generating opportunity. <br/>-a complete system to enhance governance, accountability and efficiency within their operation<br/>-52 weeks cover so no hassle to cover annual/sick .. leave<br/><br/>We would like to see designs that use the colours of our logo (green & blue).
Target Market(s)
Australian Pubs, Clubs & Hotels abookkeeping, accounting and tax services
Industry/Entity Type
Accountant
Contact Information for Business Card
Miriam Oakley CPA
Principal
Accountant Tax Agent
Miriam@KettleLedger-example.com.au
0418693142
www.kettleledger-example.com.au
Accounting / Payroll / Tax / SMSF / Technology
Colors
Designer to choose colors to be used in the design.
Look and feel
Each slider illustrates characteristics of the customer's brand and the style your logo design should communicate.

```html
<!DOCTYPE html>
<html lang="en">
<head>
<meta charset="utf-8">
<title>Kettle Ledger Business Card</title>
<link rel="stylesheet" href="https://fonts.googleapis.com/css2?family=Poppins:wght@400;500;600;700&family=Tinos&display=swap">
<style>
  :root {
    --page-bg: #dfe6ee;
    --card-bg: #f5f7f9;
    --navy: #1f2f7d;
    --green: #1c6a2e;
    --ink: #1c2a5c;
    --band-text: #e8ecf7;
    --badge-gold: #d9b53a;
    --badge-dark: #1a1a1a;
    --badge-grey: #c9ccd1;
  }
  * { box-sizing: border-box; margin: 0; padding: 0; }
  html, body { width: 1200px; height: 900px; overflow: hidden; }
  body {
    background: var(--page-bg);
    font-family: "Poppins", sans-serif;
    position: relative;
  }
  .business-card {
    position: absolute;
    left: 150px; top: 192px;
    width: 900px; height: 516px;
    background: var(--card-bg);
    box-shadow: 0 12px 36px rgba(30, 45, 80, 0.18);
  }
  .brand {
    position: absolute;
    left: 62px; top: 78px;
    display: flex; align-items: center; gap: 22px;
  }
  .brand-mark { width: 74px; height: 74px; background: var(--green); border-radius: 50%; }
  .brand-name {
    font-weight: 700; font-size: 52px; line-height: 1;
    color: var(--navy); letter-spacing: -0.5px;
  }
  .person {
    position: absolute;
    right: 60px; top: 92px;
    text-align: right;
  }
  .person-name { font-weight: 700; font-size: 26px; color: var(--navy); margin-bottom: 12px; }
  .person-role { font-weight: 500; font-size: 19px; color: var(--green); line-height: 1.45; }
  .services-rule {
    position: absolute;
    left: 62px; top: 362px;
    width: 200px; height: 2px;
    background: var(--navy);
  }
  .services-band {
    position: absolute;
    left: 236px; right: 60px; top: 330px; height: 34px;
    background: var(--navy);
    clip-path: polygon(34px 0, 100% 0, 100% 100%, 0 100%);
    display: flex; align-items: center; justify-content: flex-end;
    padding-right: 26px;
    color: var(--band-text); font-size: 20px; letter-spacing: 0.3px;
    gap: 12px;
  }
  .services-band .dot { width: 8px; height: 8px; border-radius: 50%; background: var(--band-text); }
  .contact-list {
    position: absolute;
    left: 62px; top: 382px;
    list-style: none;
    font-family: "Tinos", serif; font-size: 19px; color: var(--ink);
  }
  .contact-list li { display: flex; align-items: center; gap: 12px; height: 34px; }
  .contact-list svg { width: 17px; height: 17px; fill: var(--green); flex: none; }
  .badges {
    position: absolute;
    right: 60px; top: 430px;
    display: flex; align-items: center; gap: 10px;
  }
  .badge-pair { display: flex; }
  .badge-pair .half-a { width: 62px; height: 42px; background: var(--navy); }
  .badge-pair .half-b { width: 36px; height: 42px; background: var(--badge-gold); }
  .badge-square { width: 42px; height: 42px; background: var(--badge-dark); }
  .badge-round { width: 38px; height: 38px; border-radius: 50%; background: var(--badge-grey); border: 3px solid #8a8f96; }
</style>
</head>
<body>
  <main class="business-card">
    <div class="brand">
      <span class="brand-mark"></span>
      <span class="brand-name">Kettle Ledger</span>
    </div>

    <div class="person">
      <p class="person-name">Miriam Oakley CPA</p>
      <p class="person-role">Principal</p>
      <p class="person-role">Accountant Tax Agent</p>
    </div>

    <div class="services-rule"></div>
    <div class="services-band">
      <span>Accounting</span><span class="dot"></span>
      <span>Payroll</span><span class="dot"></span>
      <span>Tax</span><span class="dot"></span>
      <span>SMSF</span><span class="dot"></span>
      <span>Technology</span>
    </div>

    <ul class="contact-list">
      <li>
        <svg viewBox="0 0 24 24" aria-hidden="true"><path d="M6.6 10.8a15.1 15.1 0 0 0 6.6 6.6l2.2-2.2a1 1 0 0 1 1-.25 11.4 11.4 0 0 0 3.6.57 1 1 0 0 1 1 1V20a1 1 0 0 1-1 1A17 17 0 0 1 3 4a1 1 0 0 1 1-1h3.5a1 1 0 0 1 1 1c0 1.25.2 2.45.57 3.57a1 1 0 0 1-.25 1z"/></svg>
        0418693142
      </li>
      <li>
        <svg viewBox="0 0 24 24" aria-hidden="true"><path d="M2 5h20v14H2z M3.5 6.5 12 13l8.5-6.5" stroke="#f5f7f9" stroke-width="1.5"/></svg>
        Miriam@KettleLedger-example.com.au
      </li>
      <li>
        <svg viewBox="0 0 24 24" aria-hidden="true"><circle cx="12" cy="12" r="9" fill="none" stroke="#1c6a2e" stroke-width="2"/><path d="M3 12h18M12 3c3 3 3 15 0 18M12 3c-3 3-3 15 0 18" fill="none" stroke="#1c6a2e" stroke-width="1.6"/></svg>
        www.kettleledger-example.com.au
      </li>
    </ul>

    <div class="badges">
      <div class="badge-pair"><span class="half-a"></span><span class="half-b"></span></div>
      <span class="badge-square"></span>
      <span class="badge-round"></span>
    </div>
  </main>
</body>
</html>
```